Professional Photography Business cards

I need business cards that include my logo which I have uploaded. I run a photography business. I am open to ideas but I would like one side to have my logo and the other side to have my contact info. I don't have a website made but I do own a website domain. I have uploaded 2 different logo color schemes. My business colors are Blue, black , and white.

Business Name
Business Phone Number
Business Email
Business Website address
Instagram

Industry/Entity Type

Professional Photography

Contact Information for Business Card

Phone Number: 555-304-7826 email: info@tkale-studio.example Instagram: @t.kalestudio website doman- www.tkale-studio.example

Requirements
Must have
• I like the idea of a business card with a full black background front and back of card. My colors must include royal blue, black, and white

```html
<!DOCTYPE html>
<html lang="en">
<head>
<meta charset="UTF-8">
<title>T. Kale Studio – Business Cards</title>
<link href="https://fonts.googleapis.com/css2?family=Open+Sans:wght@400;600&display=swap" rel="stylesheet">
<style>
  :root {
    --stage: #1c1c1c;
    --card-white: #ffffff;
    --card-black: #141414;
    --royal-blue: #27309a;
    --ink: #2b2b2b;
    --silver: #8a8a8a;
  }
  * { margin: 0; padding: 0; box-sizing: border-box; }
  html, body {
    width: 1200px; height: 900px; overflow: hidden;
    background: var(--stage);
    font-family: "Open Sans", Arial, sans-serif;
  }
  .sheet {
    width: 1200px; height: 900px;
    display: flex; flex-direction: column;
    align-items: center; justify-content: center; gap: 48px;
  }
  .card {
    width: 560px; height: 320px;
    position: relative;
    box-shadow: 0 10px 30px rgba(0,0,0,.55);
  }
  .card--front { background: var(--card-white); display: flex; align-items: center; }
  .card--back { background: var(--card-black); display: flex; align-items: center; justify-content: center; }

  .brand { display: flex; align-items: center; gap: 12px; }
  .brand__mark {
    width: 30px; height: 30px; border-radius: 50%;
    border: 3px solid currentColor; flex: none;
  }
  .brand__name { font-weight: 600; font-size: 26px; letter-spacing: .5px; white-space: nowrap; }
  .card--front .brand { color: var(--royal-blue); padding-left: 40px; width: 275px; }
  .card--back .brand { color: var(--silver); }
  .card--back .brand__name { font-size: 34px; }
  .card--back .brand__mark { width: 40px; height: 40px; }

  .divider {
    width: 1.5px; height: 110px; background: var(--royal-blue);
    margin: 0 22px 0 6px;
  }
  .contact { list-style: none; display: flex; flex-direction: column; gap: 6px; }
  .contact__item {
    display: flex; align-items: center; gap: 8px;
    font-size: 16px; color: var(--ink);
  }
  .contact__icon { width: 13px; height: 13px; flex: none; fill: var(--royal-blue); }
</style>
</head>
<body>
<main class="sheet">
  <section class="card card--front" aria-label="Business card front">
    <div class="brand">
      <span class="brand__mark" aria-hidden="true"></span>
      <span class="brand__name">T. Kale Studio</span>
    </div>
    <div class="divider" aria-hidden="true"></div>
    <ul class="contact">
      <li class="contact__item">
        <svg class="contact__icon" viewBox="0 0 16 16" aria-hidden="true"><path d="M3.5 1l3 3-2 2c1 2 3 4 5 5l2-2 3 3-2 2C7 14 2 9 1.5 3.5z"/></svg>
        555-304-7826
      </li>
      <li class="contact__item">
        <svg class="contact__icon" viewBox="0 0 16 16" aria-hidden="true"><path d="M1 3h14v10H1z M1 3l7 6 7-6" fill="none" stroke="#27309a" stroke-width="1.8"/></svg>
        info@tkale-studio.example
      </li>
      <li class="contact__item">
        <svg class="contact__icon" viewBox="0 0 16 16" aria-hidden="true"><circle cx="8" cy="8" r="6.5" fill="none" stroke="#27309a" stroke-width="1.6"/><path d="M1.5 8h13M8 1.5c-3 3.5-3 9.5 0 13M8 1.5c3 3.5 3 9.5 0 13" fill="none" stroke="#27309a" stroke-width="1.2"/></svg>
        www.tkale-studio.example
      </li>
      <li class="contact__item">
        <svg class="contact__icon" viewBox="0 0 16 16" aria-hidden="true"><circle cx="8" cy="8" r="6"/></svg>
        @t.kalestudio
      </li>
    </ul>
  </section>

  <section class="card card--back" aria-label="Business card back">
    <div class="brand">
      <span class="brand__mark" aria-hidden="true"></span>
      <span class="brand__name">T. Kale Studio</span>
    </div>
  </section>
</main>
</body>
</html>
```